Corporate Design für Sweet Table-Service
Zielgruppe
Zwei Ladys - die eine Besitzerin eines etablierten Cafés, die andere Inhaberin eines Cake Pops-Service - wagen die gemeinsame Geschäftsgründung: Einen Service für Sweet Tables und Candy Bars. Vor allem in der Hochzeitsszene sind diese Begriffe fest etabliert. Dabei handelt es sich um eine neue Interpretation des Dessertbüffets. Die Besonderheit: Die Leckereien werden nicht einfach nur auf einem Tisch platziert, sondern der Tisch wird mit sehr viel Liebe zum Detail dekoriert und fügt sich perfekt in das Thema der Feier ein, stilistisch wie farblich. Unser Service erstreckt sich von selbst hergestellten Leckereien inklusive Cake Pops, Cupcakes, Kuchen und Torten über herkömmliche Süßigkeiten bis hin zur passenden Papeterie (inklusive Anlieferung, Aufbau und Dekoration vor Ort sowie Abholung). Der Kunde erhält also alles aus einer Hand. Und das Besondere an unserem Konzept ist, dass unser Sortiment nicht beim Süßen endet, sondern dass wir auch Pikantes anbieten. Daher auch der Name Lark'n'Lore. Wir laden Euch ein paar Fotos von Sweet Tables/Candy Bars hoch, damit Ihr einen Eindruck bekommt. Unser Internetauftritt steht schon ziemlich, befindet sich aber noch im Arbeitsmodus. Link: feierfee-muenchen.baukastenweb.com. Zur Info: Die Fotos/das Logo dienen lediglich als Platzhalter und die Domain 'larknlore.de' muss noch käuflich erworben werden.
Aufgabenstellung
Wir wünschen uns ein Corporate Design in unseren Unternehmensfarben Brombeere (rgb 77, 15, 48) und Apfelgrün (rgb 130, 185, 36). Das Logo stellen wir uns von der Form her rechteckig oder oval vor. Vom Stil her elegant und gerne auch ein wenig verspielt, aber bitte keine comicartigen Designs. Wir benötigen außerdem noch einen Untertitel/Slogan in Form von ein paar Schlagwörtern, die unseren Service beschreiben und sind für Vorschläge dankbar. Der Begriff Candy Bar sollte darin eher nicht vorkommen, da er sich für uns wenig hochwertig anhört. Das Corporate Design sollte Logo, Briefpapier und Visitenkarten umfassen. Wir freuen uns sehr auf Eure Entwürfe und sind sehr gespannt. Herzlichen Dank für Eure Arbeit!

```html
<!DOCTYPE html>
<html lang="de">
<head>
<meta charset="utf-8">
<title>Lark'n'Lore – Briefpapier</title>
<link href="https://fonts.googleapis.com/css2?family=Quicksand:wght@400;500;700&display=swap" rel="stylesheet">
<style>
  :root {
    --brombeere: rgb(77, 15, 48);
    --apfelgruen: rgb(130, 185, 36);
    --backdrop: #e6e2e8;
    --paper: #ffffff;
    --ink: #4d0f30;
    --pattern-light: rgba(200, 196, 202, 0);
    --pattern-tone: rgba(200, 196, 202, 0.35);
  }
  * { box-sizing: border-box; margin: 0; padding: 0; }
  html, body {
    width: 1200px; height: 899px; overflow: hidden;
    background: var(--backdrop);
    font-family: "Quicksand", sans-serif;
    color: var(--ink);
  }
  .letterhead {
    position: absolute; left: 296px; top: 20px;
    width: 608px; height: 860px;
    background: var(--paper);
    box-shadow: 0 6px 24px rgba(60, 40, 60, 0.15);
    overflow: hidden;
  }
  .brand-mark {
    position: absolute; left: 430px; top: 48px; width: 132px;
    display: flex; align-items: center; gap: 8px;
  }
  .brand-mark__dot {
    width: 12px; height: 12px; border-radius: 50%;
    background: var(--brombeere); flex: none;
  }
  .brand-mark__name {
    font-weight: 700; font-size: 22px; color: var(--brombeere);
    white-space: nowrap;
  }
  .contact-block {
    position: absolute; left: 440px; top: 128px;
    font-size: 8.5px; line-height: 1.45;
  }
  .contact-block__company { font-weight: 700; color: var(--brombeere); }
  .contact-block__owners { font-weight: 500; color: var(--apfelgruen); margin-bottom: 10px; }
  .contact-block__address { margin-bottom: 10px; }
  .contact-row { display: flex; align-items: center; gap: 6px; }
  .contact-row svg { width: 9px; height: 9px; flex: none; }
  .contact-row--spaced { margin-top: 8px; }
  .contact-row__web { font-weight: 700; }
  .sender-line {
    position: absolute; left: 70px; top: 186px;
    font-size: 7px; letter-spacing: 0.1px;
  }
  .sender-line strong { font-weight: 700; }
  .fold-mark {
    position: absolute; left: 0; width: 14px; height: 1px;
    background: var(--apfelgruen);
  }
  .fold-mark--upper { top: 304px; }
  .fold-mark--middle { top: 430px; }
  .fold-mark--lower { top: 608px; }
  .footer-pattern {
    position: absolute; left: 0; right: 0; bottom: 0; height: 130px;
    background: linear-gradient(to bottom, var(--pattern-light), var(--pattern-tone));
  }
  .footer {
    position: absolute; left: 70px; right: 40px; bottom: 34px;
    display: flex; justify-content: space-between;
    font-size: 6.5px; line-height: 1.45;
  }
  .footer__label { font-weight: 700; color: var(--apfelgruen); }
</style>
</head>
<body>
  <main class="letterhead">
    <div class="brand-mark">
      <span class="brand-mark__dot"></span>
      <span class="brand-mark__name">Lark'n'Lore</span>
    </div>

    <address class="contact-block" style="font-style:normal">
      <div class="contact-block__company">lark'n'lore</div>
      <div class="contact-block__owners">Nora Falkner &amp; Ines Brandt</div>
      <div class="contact-block__address">Amselweg 42<br>80937 München</div>
      <div class="contact-row">
        <svg viewBox="0 0 10 10" aria-hidden="true"><path d="M2 1 L4 3 L3 4 Q4 6 6 7 L7 6 L9 8 L8 9 Q3 9 1 2 Z" fill="none" stroke="var(--apfelgruen)" stroke-width="0.9"/></svg>
        <span>NF &nbsp;+49 (0)170 5550142</span>
      </div>
      <div class="contact-row">
        <svg viewBox="0 0 10 10" aria-hidden="true"><path d="M2 1 L4 3 L3 4 Q4 6 6 7 L7 6 L9 8 L8 9 Q3 9 1 2 Z" fill="none" stroke="var(--apfelgruen)" stroke-width="0.9"/></svg>
        <span>IB &nbsp;+49 (0)151 5550187</span>
      </div>
      <div class="contact-row contact-row--spaced">
        <svg viewBox="0 0 10 10" aria-hidden="true"><rect x="1" y="2.5" width="8" height="5.5" fill="none" stroke="var(--apfelgruen)" stroke-width="0.9"/><path d="M1 2.5 L5 6 L9 2.5" fill="none" stroke="var(--apfelgruen)" stroke-width="0.9"/></svg>
        <span>service@larknlore.de</span>
      </div>
      <div class="contact-row">
        <svg viewBox="0 0 10 10" aria-hidden="true"><path d="M1.5 5 L5 1.5 L8.5 5 M2.5 4.5 V8.5 H7.5 V4.5" fill="none" stroke="var(--apfelgruen)" stroke-width="0.9"/></svg>
        <span class="contact-row__web">www.larknlore.de</span>
      </div>
    </address>

    <p class="sender-line"><strong>lark'n'lore</strong> · Amselweg 42 · 80937 München</p>

    <span class="fold-mark fold-mark--upper"></span>
    <span class="fold-mark fold-mark--middle"></span>
    <span class="fold-mark fold-mark--lower"></span>

    <div class="footer-pattern" role="img" aria-label="Dezentes Muster aus hellgrauen Schlagwörtern zum Angebot"></div>

    <footer class="footer">
      <div class="footer__col">
        <div><span class="footer__label">GF:</span> Nora Falkner &amp; Ines Brandt</div>
        <div><span class="footer__label">USt.-ID:</span> DE 123 456 789</div>
        <div><span class="footer__label">Amtsgericht Musterburg:</span> HRA 12345</div>
      </div>
      <div class="footer__col">
        <div class="footer__label">Isartal Bank</div>
        <div>IBAN DE00000000 0000 0000 0000 00</div>
        <div>BIC XXXXXXXXXXX</div>
      </div>
      <div class="footer__col">
        <div class="footer__label">Nordbank München</div>
        <div>IBAN DE00000000 0000 0000 0000 00</div>
        <div>BIC XXXXXXXXXXX</div>
      </div>
      <div class="footer__col">
        <div class="footer__label">Kreiskasse Oberland</div>
        <div>IBAN DE00000000 0000 0000 0000 00</div>
        <div>BIC XXXXXXXXXXX</div>
      </div>
    </footer>
  </main>
</body>
</html>
```